Redesign Current Website Into An Exciting Updated Design

We need to redesign the current website www.gleamvoucherhub.com We want an overall new look. We are rebranding so it will be a new logo and we would like to see new images as well so you cannot compare the old from the new.

You can use same exact content as on current url www.gleamvoucherhub.com

The website must be warm and inviting and fun yet professional and modern.

The website must also be designed with mobile in mind

The website must be warm and inviting yet professional and modern.

The website must also be designed with mobile in mind.

Target Market(s)

Consumers redeeming rewards

Industry/Entity Type

Promotional Reward Fullfillment

Coding

Coded - Design and coding required

Number of Pages Required

3 page

Requirements
Must have
• This website is a website where consumers come to redeem rewards they received from doing business with a company that offers these rewards. So the website should be very inviting.
Nice to have
• open
Should not have
• open

```html
<!DOCTYPE html>
<html lang="en">
<head>
<meta charset="utf-8">
<title>Gleam Voucher Hub – Online Redemption System</title>
<link href="https://fonts.googleapis.com/css2?family=Bebas+Neue&family=Poppins:ital,wght@0,400;0,500;0,600;1,400&display=swap" rel="stylesheet">
<style>
:root{
  --blue:#2a6395;
  --blue-dark:#1f4f7c;
  --footer:#2b6698;
  --footer-bottom:#235985;
  --ink:#1b1b1b;
  --light:#f6f6f6;
  --white:#ffffff;
  --star:#f2b705;
}
*{box-sizing:border-box;margin:0;padding:0}
html,body{width:1200px;height:3795px;overflow:hidden}
body{position:relative;font-family:"Poppins",sans-serif;color:var(--ink);background:var(--white)}
.abs{position:absolute}
.display{font-family:"Bebas Neue",sans-serif;font-weight:400;letter-spacing:.5px}

.topbar{left:0;top:0;width:1200px;height:44px;background:var(--blue);color:#fff;font-size:14px}
.topbar .phone{left:69px;top:12px;display:flex;gap:10px;align-items:center}
.topbar .mail{right:69px;top:12px;display:flex;gap:10px;align-items:center}
.navbar{left:0;top:44px;width:1200px;height:55px;background:#fff;font-size:13px;font-weight:500}
.navbar ul{list-style:none;display:flex;gap:30px;position:absolute;top:19px}
.nav-left{left:66px}
.nav-right{right:66px}
.brand-badge{left:468px;top:0;width:262px;height:194px;z-index:5}
.brand-name{left:468px;top:66px;width:262px;text-align:center;color:#fff;font-size:31px;line-height:30px;z-index:6}

.hero{left:0;top:99px;width:1200px;height:748px;background:linear-gradient(100deg,#f4f1ec 0%,#f0ebe2 40%,#e9eef0 70%,#f7f7f7 100%)}
.hero-welcome{left:68px;top:236px;font-size:40px;color:var(--ink)}
.hero-title{left:68px;top:284px;font-size:104px;line-height:104px;color:var(--blue)}
.hero-text{left:68px;top:612px;width:420px;font-size:14px;line-height:26.5px;color:var(--blue);font-weight:500}
.photo{position:absolute;border-radius:29px}

.redeem-form{left:66px;top:798px;width:756px;height:96px;border-radius:35px;background:var(--blue);overflow:hidden}
.redeem-form .field{position:absolute;top:21px;height:54px;background:#fff;font-size:12px;font-weight:600;padding:19px 18px;color:var(--ink)}
.redeem-form .go{position:absolute;left:600px;top:0;width:156px;height:96px;background:var(--blue-dark);color:#fff;font-size:30px;font-weight:600;display:flex;align-items:center;justify-content:center;gap:14px}

.card{position:absolute;border-radius:22px;overflow:hidden}
.card .label{position:absolute;left:0;right:0;bottom:22px;text-align:center;color:#fff;font-size:25px;font-weight:500;line-height:30px}
.card .shade{position:absolute;inset:0;background:linear-gradient(180deg,rgba(0,0,0,0) 55%,rgba(0,0,0,.55) 100%)}

.btn{position:absolute;background:var(--blue);color:#fff;border-radius:40px;display:flex;align-items:center;justify-content:center;gap:14px;font-weight:600}

.about{left:0;top:1858px;width:1200px;height:627px;background:var(--light)}
.eyebrow{font-size:20px;color:var(--blue);font-weight:500;display:flex;align-items:center;gap:12px}
.eyebrow .rule{display:inline-block;width:40px;height:2px;background:var(--blue)}
.section-title{font-size:62px;line-height:62px;color:var(--blue)}
.about-text{left:633px;top:2104px;width:500px;font-size:15px;line-height:26.5px;color:#333;text-align:justify}

.review{position:absolute;top:2591px;width:320px;height:251px;background:#fff;box-shadow:0 3px 14px rgba(0,0,0,.12);padding:32px 20px 0 26px}
.review p{font-size:14px;line-height:24px;font-style:italic;color:#333;white-space:nowrap}
.review .who{position:absolute;left:26px;top:163px;display:flex;gap:14px;align-items:center}
.review .avatar{width:64px;height:64px;border-radius:50%;background:linear-gradient(135deg,#c7a58a,#8a6a55)}
.review .name{color:var(--blue);font-size:17px;font-weight:500}
.review .stars{color:var(--star);font-size:13px;letter-spacing:2px}
.review .quote{position:absolute;right:22px;bottom:18px}

.round-arrow{position:absolute;width:44px;height:44px;border-radius:50%;display:flex;align-items:center;justify-content:center}
.round-arrow.outline{border:2px solid var(--blue);background:#fff}
.round-arrow.solid{background:var(--blue)}

.clients{left:0;top:2952px;width:1200px;height:439px;background:var(--light)}
.client-box{position:absolute;top:3229px;width:209px;height:87px;background:#fff;border:1px solid #e2e2e2;display:flex;align-items:center;justify-content:center;gap:10px;font-size:17px;font-weight:600;color:var(--blue)}
.client-box .dot{width:16px;height:16px;border-radius:50%;background:var(--blue)}

.footer{left:0;top:3391px;width:1200px;height:343px;background:var(--footer);color:#fff}
.footer-bottom{left:0;top:3734px;width:1200px;height:61px;background:var(--footer-bottom);color:#fff;font-size:12px}
.f-head{font-size:21px;color:#fff}
.f-head::after{content:"";display:block;width:34px;height:2px;background:#fff;margin-top:6px}
.f-list{list-style:none;font-size:14px;line-height:26px}
.f-list li{display:flex;gap:10px;align-items:center}
.contact-row{display:flex;gap:16px;font-size:14px;line-height:16px;margin-bottom:18px}
.contact-row .ico{width:22px;height:22px;border:1px solid #fff;border-radius:4px;display:flex;align-items:center;justify-content:center;flex:none}
.social{position:absolute;top:3747px;width:25px;height:25px;border:1px solid #fff;border-radius:3px;background:var(--footer-bottom)}
</style>
</head>
<body>

<div class="abs topbar">
  <div class="abs phone">
    <svg width="15" height="15" viewBox="0 0 24 24"><path d="M6.6 10.8a15 15 0 0 0 6.6 6.6l2.2-2.2a1 1 0 0 1 1-.25 11.4 11.4 0 0 0 3.6.6 1 1 0 0 1 1 1V20a1 1 0 0 1-1 1A17 17 0 0 1 3 4a1 1 0 0 1 1-1h3.5a1 1 0 0 1 1 1c0 1.25.2 2.45.6 3.6a1 1 0 0 1-.25 1z" fill="#fff"/></svg>
    <span>8012 345 6789</span>
  </div>
  <div class="abs mail">
    <svg width="20" height="14" viewBox="0 0 20 14"><rect x="1" y="1" width="18" height="12" fill="none" stroke="#fff" stroke-width="1.6"/><path d="M1 1l9 7 9-7" fill="none" stroke="#fff" stroke-width="1.6"/></svg>
    <span>info@websitename.com</span>
  </div>
</div>

<nav class="abs navbar">
  <ul class="nav-left"><li>HOME</li><li>ABOUT US</li><li>SERVICES</li><li>TESTIMONIALS</li></ul>
  <ul class="nav-right"><li>ALREADY REDEEMED?</li><li>HELP</li><li>CONTACT US</li></ul>
</nav>

<section class="abs hero" role="img" aria-label="Faded photo of a smiling traveller with arms spread out"></section>

<svg class="abs brand-badge" viewBox="0 0 262 194"><path d="M0 0H262V140L131 194L0 140Z" fill="var(--blue)"/><rect x="62" y="52" width="138" height="84" fill="none" stroke="#fff" stroke-width="2"/></svg>
<div class="abs brand-name display">GLEAM<br>VOUCHER HUB</div>

<div class="abs hero-welcome display">WELCOME TO</div>
<h1 class="abs hero-title display">THE ONLINE<br>REDEMPTION<br>SYSTEM</h1>
<p class="abs hero-text">To Learn More About Your Offer Including The Full Details, How It Works, Terms, FAQ's and To Redeem and Activate Your Certificate Please Enter A Valid Certificate Number and Email.</p>

<div class="photo" style="left:671px;top:222px;width:208px;height:255px;background:linear-gradient(180deg,#5fb2e6,#2a9fb0 55%,#8a6a4a)" role="img" aria-label="Wooden pier leading to a tropical island"></div>
<div class="photo" style="left:900px;top:222px;width:300px;height:255px;border-radius:29px 0 0 29px;background:linear-gradient(160deg,#7cc1e8,#2fc2c4 50%,#e5dccb)" role="img" aria-label="Aerial view of a turquoise beach from a plane window"></div>
<div class="photo" style="left:534px;top:490px;width:349px;height:256px;background:linear-gradient(180deg,#6e8a6a,#2f8f95 55%,#4a3b30)" role="img" aria-label="Woman in a hat sitting in a boat among limestone cliffs"></div>
<div class="photo" style="left:900px;top:490px;width:244px;height:256px;background:linear-gradient(180deg,#2c4a7a,#c8834a 55%,#1f5f7a)" role="img" aria-label="Overwater bungalows lit up at dusk"></div>

<form class="abs redeem-form">
  <div class="field" style="left:40px;width:274px">CERTIFICATE ID</div>
  <div class="field" style="left:323px;width:275px">ENTER EMAIL ADDRESS</div>
  <div class="go">GO <svg width="16" height="10" viewBox="0 0 16 10"><path d="M0 5h14M10 1l4 4-4 4" fill="none" stroke="#fff" stroke-width="2"/></svg></div>
</form>

<div class="card" style="left:68px;top:970px;width:341px;height:284px;background:linear-gradient(180deg,#5d8fd8,#5a7b4a 45%,#2fb0c0 75%,#1b5b73)" role="img" aria-label="Tropical island with overwater villas"><div class="shade"></div><div class="label">Vacation Certificates</div></div>
<div class="card" style="left:430px;top:970px;width:340px;height:284px;background:linear-gradient(180deg,#2f6fc4,#7fb0e6 55%,#c9dff2)" role="img" aria-label="Passenger jet flying above clouds"><div class="shade"></div><div class="label">Travel Vouchers</div></div>
<div class="card" style="left:792px;top:970px;width:342px;height:284px;background:linear-gradient(160deg,#e8e4e0,#b7b3b2 50%,#2e3c52)" role="img" aria-label="Hand holding a tablet"><div class="shade"></div><div class="label">Digital Electronic<br>Products</div></div>
<div class="card" style="left:68px;top:1272px;width:341px;height:358px;background:linear-gradient(180deg,#3d3535,#a24a3a 50%,#1f2430)" role="img" aria-label="Dining table with flowers and pendant lights"><div class="shade"></div><div class="label">Dining Incentives</div></div>
<div class="card" style="left:428px;top:1272px;width:706px;height:358px;background:linear-gradient(90deg,#2a2a30,#6b5a4a 35%,#c9a040 50%,#6b5a4a 65%,#2a2a30)" role="img" aria-label="Woman shopping with a cart in a grocery aisle"><div class="shade"></div><div class="label">Gas &amp; Grocery Rewards</div></div>

<div class="btn" style="left:433px;top:1693px;width:334px;height:68px;font-size:18px">REDEEM YOUR OFFER NOW <svg width="16" height="10" viewBox="0 0 16 10"><path d="M0 5h14M10 1l4 4-4 4" fill="none" stroke="#fff" stroke-width="2"/></svg></div>

<section class="abs about"></section>
<div class="photo" style="left:68px;top:1942px;width:380px;height:323px;border-radius:22px;background:linear-gradient(180deg,#1f3f7a,#3a4f6a 50%,#b06a40 75%,#1a2840)" role="img" aria-label="City waterfront skyline at night"></div>
<div class="photo" style="left:199px;top:2135px;width:296px;height:253px;border-radius:22px;border:4px solid #fff;background:linear-gradient(90deg,#7a5a3a,#d8c8a8 50%,#8a6a4a)" role="img" aria-label="Luxury hotel lobby with chandelier"></div>
<div class="photo" style="left:318px;top:1985px;width:243px;height:206px;border-radius:22px;border:4px solid #fff;background:linear-gradient(180deg,#6e8a6a,#2f8f95 55%,#4a3b30)" role="img" aria-label="Woman in a hat sitting in a boat among cliffs"></div>

<div class="abs eyebrow" style="left:636px;top:1985px">Who We are <span class="rule"></span></div>
<h2 class="abs section-title display" style="left:633px;top:2016px">ABOUT US</h2>
<p class="abs about-text">We provide marketing incentives in the form of gift certificates and vouchers that are redeemable for a variety of items such as: discount travel, smart device products, restaurant incentives , golf discounts and more to thousands of businesses around the world who use them to create exciting marketing promotions and giveaways, customer loyalty programs, promotional contests and use them as customer appreciation gifts.</p>
<div class="btn" style="left:633px;top:2323px;width:155px;height:36px;font-size:13px">READ MORE <svg width="16" height="10" viewBox="0 0 16 10"><path d="M0 5h14M10 1l4 4-4 4" fill="none" stroke="#fff" stroke-width="2"/></svg></div>

<div class="abs eyebrow" style="left:99px;top:2601px">Reviews <span class="rule"></span></div>
<h2 class="abs section-title display" style="left:97px;top:2636px">TESTIMONIALS</h2>
<div class="round-arrow outline" style="left:96px;top:2779px"><svg width="10" height="14" viewBox="0 0 10 14"><path d="M8 1L2 7l6 6" fill="none" stroke="var(--blue)" stroke-width="2.4"/></svg></div>
<div class="round-arrow solid" style="left:149px;top:2779px"><svg width="10" height="14" viewBox="0 0 10 14"><path d="M2 1l6 6-6 6" fill="none" stroke="#fff" stroke-width="2.4"/></svg></div>

<div class="review" style="left:458px">
  <p>Lorem ipsum dolor sit amet, consecte<br>tur adipiscing elit. Pellentesque aliquet<br>eros vitae placerat hendrerit. Maece<br>nas maximus commodo sapien, vitae<br>lobortis ligula</p>
  <div class="who"><div class="avatar" role="img" aria-label="Reviewer portrait"></div><div><div class="name">Marcus Hale</div><div class="stars">★★★★★</div></div></div>
  <svg class="quote" width="40" height="32" viewBox="0 0 40 32"><path d="M0 0h16v16l-6 16H2l5-14H0zM22 0h16v16l-6 16h-8l5-14h-7z" fill="var(--blue)"/></svg>
</div>
<div class="review" style="left:811px">
  <p>Lorem ipsum dolor sit amet, consecte<br>tur adipiscing elit. Pellentesque aliquet<br>eros vitae placerat hendrerit. Maece<br>nas maximus commodo sapien, vitae<br>lobortis ligula</p>
  <div class="who"><div class="avatar" style="background:linear-gradient(135deg,#e6c9a8,#b08a6a)" role="img" aria-label="Reviewer portrait"></div><div><div class="name">Delia Fenn</div><div class="stars">★★★★★</div></div></div>
  <svg class="quote" width="40" height="32" viewBox="0 0 40 32"><path d="M0 0h16v16l-6 16H2l5-14H0zM22 0h16v16l-6 16h-8l5-14h-7z" fill="var(--blue)"/></svg>
</div>

<section class="abs clients"></section>
<div class="abs eyebrow" style="left:512px;top:3034px"><span class="rule"></span> Clients <span class="rule"></span></div>
<h2 class="abs section-title display" style="left:0;width:1200px;text-align:center;top:3068px">OUR CLIENTS</h2>
<p class="abs" style="left:0;width:1200px;text-align:center;top:3161px;font-size:16px">A few of our clients that we redeem and fulfill gift certificates and rewards for</p>
<div class="round-arrow outline" style="left:66px;top:3255px"><svg width="10" height="14" viewBox="0 0 10 14"><path d="M8 1L2 7l6 6" fill="none" stroke="var(--blue)" stroke-width="2.4"/></svg></div>
<div class="client-box" style="left:149px"><span class="dot"></span>Roamwell Trips</div>
<div class="client-box" style="left:381px">Fieldline Coaches</div>
<div class="client-box" style="left:613px">Keystone Homes</div>
<div class="client-box" style="left:842px"><span class="dot"></span>Orvane Motors</div>
<div class="round-arrow solid" style="left:1088px;top:3255px"><svg width="10" height="14" viewBox="0 0 10 14"><path d="M2 1l6 6-6 6" fill="none" stroke="#fff" stroke-width="2.4"/></svg></div>

<footer class="abs footer">
  <div class="abs" style="left:122px;top:106px;width:172px;height:149px">
    <svg width="172" height="149" viewBox="0 0 172 149" class="abs" style="left:0;top:0"><rect x="4" y="40" width="164" height="105" fill="none" stroke="#fff" stroke-width="2"/></svg>
    <div class="abs display" style="left:0;top:62px;width:172px;text-align:center;font-size:34px;line-height:32px">GLEAM<br>VOUCHER HUB</div>
  </div>

  <div class="abs" style="left:399px;top:90px">
    <div class="f-head display">QUICK LINKS</div>
    <ul class="f-list" style="margin-top:22px">
      <li>› About Us</li><li>› Services</li><li>› Testimonials</li><li>› Already Redeemed</li><li>› Help</li>
    </ul>
  </div>

  <div class="abs" style="left:612px;top:90px">
    <div class="f-head display">CONTACT US</div>
    <div style="margin-top:22px">
      <div class="contact-row"><span class="ico"><svg width="12" height="12" viewBox="0 0 24 24"><path d="M6.6 10.8a15 15 0 0 0 6.6 6.6l2.2-2.2a1 1 0 0 1 1-.25 11.4 11.4 0 0 0 3.6.6 1 1 0 0 1 1 1V20a1 1 0 0 1-1 1A17 17 0 0 1 3 4a1 1 0 0 1 1-1h3.5a1 1 0 0 1 1 1c0 1.25.2 2.45.6 3.6a1 1 0 0 1-.25 1z" fill="#fff"/></svg></span><div>CALL US<br>012 345 6789</div></div>
      <div class="contact-row"><span class="ico"><svg width="12" height="9" viewBox="0 0 20 14"><rect x="1" y="1" width="18" height="12" fill="#fff"/><path d="M1 1l9 7 9-7" fill="none" stroke="var(--footer)" stroke-width="1.6"/></svg></span><div>EMAIL US<br>info@websitename.com</div></div>
      <div class="contact-row"><span class="ico"><svg width="10" height="13" viewBox="0 0 10 14"><path d="M5 0a5 5 0 0 1 5 5c0 4-5 9-5 9S0 9 0 5a5 5 0 0 1 5-5z" fill="#fff"/><circle cx="5" cy="5" r="2" fill="var(--footer)"/></svg></span><div>address line dummy here<br>Address line dummy</div></div>
    </div>
  </div>

  <div class="abs" style="left:919px;top:90px;width:200px">
    <div class="f-head display">OUR NEWSLETTER</div>
    <p style="margin-top:22px;font-size:14px;line-height:16px">Subscribe our newsletter to get the latest news.</p>
    <div style="margin-top:20px;width:195px;height:30px;background:#fff"></div>
    <div style="margin-top:19px;width:111px;height:29px;border:1px solid #fff;border-radius:20px;font-size:13px;text-align:center;line-height:27px">SUBSCRIBE</div>
  </div>
</footer>

<div class="abs footer-bottom"><span class="abs" style="left:69px;top:22px">Copyright © 2025 All Rights Reserved By Company Name</span></div>
<div class="social" style="left:1014px"></div>
<div class="social" style="left:1045px"></div>
<div class="social" style="left:1077px"></div>
<div class="social" style="left:1109px"></div>

</body>
</html>
```